Website Redesign for Allies of Beit Norah

Beit Norah's mission is to enable chronically ill, disabled, infirm, and terminally ill people in Israel to live with dignity. Allies of Beit Norah raises awareness of and funds for Beit Norah to its friends in the USA. This project is to redesign Allies of Beit Norah's current site (https://alliesofbeitnorah.example/).

The redesigned site will use current colors, logo, and text, but will get new images. The design must 1) project a friendlier vibe, 2) be emotionally engaging and inviting (so people will make donations), and 3) be clear (so people get an understanding of Beit Norah at a glance).

Please provide a homepage design and one inner page design.
Please provide PSD files so we can see all layers of the design.
Please take the colors from the current logo.

Target Market(s)

high net worth individuals who are interested in Israel, Jewish causes, philanthropic elder care and medical care.

Industry/Entity Type

non-profit fundraising organization for old and young in Israel who are chronically ill, disabled, infirm, and terminally ill.

Number of Pages Required

2 page

Font styles to use
Sans Serif

Colors
0054AA
0677BA
7BADD7
CADEEF
E8F1F8
EB3D1F
EC4F4E
F09395
F8D3D4
FCEDEE

Requirements
Must have
• PSD files. site colors from logo (red and blue). friendly, emotionally engaging and clear so people will donate.
Should not have
• not too flashy - target market is older

```html
<!DOCTYPE html>
<html lang="en">
<head>
<meta charset="utf-8">
<title>Allies of Beit Norah – Home</title>
<link rel="stylesheet" href="https://fonts.googleapis.com/css2?family=Montserrat:wght@500;600;700;800&family=Poppins:wght@400;500;600&display=swap">
<style>
:root{
  --navy:#16217a;
  --blue:#0054aa;
  --blue-mid:#0677ba;
  --blue-soft:#7badd7;
  --blue-pale:#cadeef;
  --blue-mist:#e8f1f8;
  --red:#eb3d1f;
  --red-soft:#ec4f4e;
  --ink:#1d1f3a;
  --muted:#55586e;
  --white:#fff;
  --head:"Montserrat",sans-serif;
  --body:"Poppins",sans-serif;
}
*{box-sizing:border-box;margin:0;padding:0}
html,body{width:1200px;height:5212px;overflow:hidden}
body{font-family:var(--body);color:var(--ink);background:var(--white);position:relative}
section,header,footer{position:absolute;left:0;width:1200px}
.btn{display:inline-block;font-family:var(--head);font-weight:700;font-size:13px;letter-spacing:.06em;text-transform:uppercase;border-radius:30px;padding:13px 28px}
.btn-red{background:var(--red);color:var(--white)}
.btn-outline{border:2px solid var(--navy);color:var(--navy);background:var(--white)}
.eyebrow{font-family:var(--head);font-weight:600;font-size:14px;letter-spacing:.14em;color:var(--red);text-transform:uppercase}
.title{font-family:var(--head);font-weight:800;font-size:38px;line-height:1.12;color:var(--navy);text-transform:uppercase}
.title .accent{color:var(--red)}
.copy{font-size:16px;line-height:1.7;color:var(--muted)}
.photo{position:absolute}

/* header */
.site-header{top:0;height:112px;background:var(--white);z-index:5;box-shadow:0 2px 10px rgba(0,0,0,.06)}
.topline{position:absolute;left:0;right:0;top:0;height:40px;display:flex;align-items:center;padding:0 60px;font-family:var(--head);font-size:12px;font-weight:700;color:var(--navy)}
.topline .dots{display:flex;gap:8px}
.topline .dots span{width:18px;height:18px;border-radius:50%;background:var(--navy)}
.topline .right{margin-left:auto;display:flex;gap:30px}
.brand{position:absolute;left:60px;top:46px;display:flex;align-items:center;gap:12px}
.brand .mark{width:36px;height:36px;border-radius:50%;background:var(--red)}
.brand .name{font-family:var(--head);font-weight:800;font-size:21px;line-height:1;color:var(--navy)}
.nav{position:absolute;right:60px;top:60px;display:flex;align-items:center;gap:34px;font-family:var(--head);font-weight:700;font-size:13px;color:var(--navy);text-transform:uppercase}
.nav .active{color:var(--red)}
.nav .btn{padding:11px 24px;font-size:12px}

/* hero */
.hero{top:0;height:740px;overflow:hidden;background:var(--navy)}
.hero-photo{left:0;top:112px;width:1200px;height:520px;background:linear-gradient(120deg,#c9b9a8 0%,#8c7e78 40%,#b8a79a 70%,#6f6a70 100%)}
.hero-swoop{position:absolute;left:0;top:420px}
.hero-box{position:absolute;left:200px;top:280px;width:800px;text-align:center}
.hero-tag{display:inline-block;background:var(--red);color:var(--white);font-family:var(--head);font-weight:700;font-size:15px;letter-spacing:.12em;padding:8px 28px;text-transform:uppercase}
.hero-title{font-family:var(--head);font-weight:800;font-size:44px;line-height:1.15;color:var(--white);text-transform:uppercase;margin-top:14px}
.hero-box .btn{margin-top:22px;background:var(--blue);color:var(--white);padding:10px 22px;font-size:12px}
.stats{position:absolute;left:60px;right:60px;top:600px;display:flex;justify-content:space-between;color:var(--white);text-align:center}
.stat{width:200px}
.stat svg{display:block;margin:0 auto 8px}
.stat b{display:block;font-family:var(--head);font-weight:800;font-size:30px}
.stat small{display:block;font-size:11px;font-weight:600;letter-spacing:.06em;text-transform:uppercase;margin-top:2px}

/* care */
.care{top:740px;height:580px}
.care-ring{position:absolute;left:60px;top:20px;width:540px;height:540px;border-radius:50%;border:3px solid var(--red-soft)}
.care-photo{left:80px;top:40px;width:500px;height:500px;border-radius:50%;background:radial-gradient(circle at 50% 40%,#d6c4b4,#8d7f77)}
.care-text{position:absolute;left:630px;top:80px;width:520px}
.care-text .title{margin:8px 0 20px}
.care-text .btn{margin-top:22px}

/* donate */
.donate{top:1320px;height:540px;background:var(--navy)}
.donate-photo{left:0;top:0;width:600px;height:540px;background:linear-gradient(135deg,#e3d7cc,#b49c8c 60%,#8a7a70)}
.donate-form{position:absolute;left:660px;top:60px;width:480px}
.donate-form .eyebrow{color:var(--white)}
.donate-form .title{color:var(--white);margin:6px 0 10px}
.donate-form p{color:var(--white);font-size:16px}
.amounts{display:grid;grid-template-columns:repeat(3,1fr);gap:12px;margin-top:18px}
.amt{background:var(--white);color:var(--ink);font-weight:600;font-size:15px;padding:11px 16px;border-radius:4px}
.amt.on{background:var(--red);color:var(--white)}
.amt.wide{grid-column:span 2}
.monthly{display:flex;align-items:center;gap:10px;color:var(--white);font-size:12px;margin-top:14px}
.monthly i{width:14px;height:14px;background:var(--white);display:block}
.donate-form .btn{margin-top:18px}

/* involved */
.involved{top:1880px;height:540px}
.involved-text{position:absolute;left:60px;top:110px;width:540px}
.involved-text .title{margin:8px 0 22px;font-size:36px}
.involved-text .btn{margin-top:22px}
.involved-photo{left:620px;top:20px;width:580px;height:500px;border-radius:0 0 0 90px;background:linear-gradient(150deg,#b9b0a8,#7f7570 60%,#5f5a5e)}

/* news */
.news{top:2420px;height:660px;background:var(--blue-mist)}
.news-head{text-align:center;padding-top:40px}
.news-head .title{margin-top:6px}
.cards{position:absolute;left:100px;top:150px;display:flex;gap:41px}
.card{width:306px;background:var(--white);box-shadow:0 8px 20px rgba(22,33,122,.08)}
.card .thumb{height:220px;background:linear-gradient(135deg,#d9c7b8,#8d7b70)}
.card.feature .thumb{background:linear-gradient(135deg,#6d6a80,#2b2f5e)}
.card .body{position:relative;padding:30px 22px 24px;text-align:center}
.card .date{position:absolute;left:50%;top:-16px;transform:translateX(-50%);background:var(--red);color:var(--white);font-size:12px;font-weight:600;padding:6px 16px}
.card h3{font-family:var(--head);font-weight:700;font-size:16px;line-height:1.35;color:var(--navy)}
.card p{font-size:12px;line-height:1.6;color:var(--muted);margin-top:10px}
.card .more{display:block;font-family:var(--head);font-weight:700;font-size:11px;color:var(--navy);text-decoration:underline;margin-top:12px}
.card.feature{background:var(--navy)}
.card.feature h3,.card.feature p,.card.feature .more{color:var(--white)}

/* impact */
.impact{top:3100px;height:600px}
.impact-frame{position:absolute;left:120px;top:120px;width:360px;height:420px;background:var(--navy)}
.impact-photo{left:160px;top:80px;width:360px;height:380px;background:linear-gradient(140deg,#d9d0c6,#8f7f6c 55%,#c9a560)}
.impact-text{position:absolute;left:660px;top:90px;width:480px}
.impact-text .title{font-size:26px;margin:6px 0 26px}
.point{display:flex;gap:18px;margin-bottom:24px}
.point .dot{flex:none;width:50px;height:50px;border-radius:50%;background:var(--navy);display:flex;align-items:center;justify-content:center}
.point h4{font-family:var(--head);font-weight:700;font-size:14px;color:var(--navy);text-transform:uppercase}
.point p{font-size:13px;line-height:1.6;color:var(--muted);margin-top:6px}

/* profile */
.profile{top:3700px;height:540px;background:var(--blue-mist)}
.profile-head{text-align:center;padding-top:40px}
.profile-head .title{margin-top:6px}
.badges{position:absolute;left:120px;top:160px;display:flex;gap:40px}
.badge-card{width:460px;height:340px;background:var(--white);text-align:center;padding-top:40px}
.badge-card .seal{width:140px;height:140px;border-radius:50%;background:var(--blue-pale);margin:0 auto}
.badge-card .plate{width:200px;height:130px;background:var(--blue-pale);margin:5px auto 0}
.badge-card h4{font-family:var(--head);font-weight:800;font-size:16px;color:var(--navy);text-transform:uppercase;margin-top:30px}
.badge-card p{font-size:13px;color:var(--muted);line-height:1.55;width:360px;margin:8px auto 0}

/* contact */
.contact{top:4240px;height:520px}
.contact-text{position:absolute;left:110px;top:40px;width:500px}
.contact-text .title{margin:6px 0 26px;font-size:32px}
.line{display:flex;align-items:center;gap:16px;margin-bottom:16px}
.line .ic{width:42px;height:42px;flex:none;border-radius:50%;background:var(--red);display:flex;align-items:center;justify-content:center}
.line small{display:block;font-size:12px;color:var(--muted)}
.line span{font-size:14px;font-weight:500;color:var(--navy)}
.subscribe-label{font-size:14px;font-weight:600;color:var(--navy);margin-top:18px}
.subscribe{display:flex;margin-top:12px;width:440px;border:1px solid var(--blue-pale);border-radius:30px;overflow:hidden}
.subscribe span{flex:1;padding:13px 22px;font-size:13px;color:var(--muted)}
.subscribe b{background:var(--navy);color:var(--white);font-family:var(--head);font-size:12px;padding:13px 24px;text-transform:uppercase}
.contact-ring{position:absolute;left:620px;top:0;width:500px;height:500px;border-radius:50%;border:3px solid var(--red-soft)}
.contact-photo{left:640px;top:20px;width:460px;height:460px;border-radius:50%;background:radial-gradient(circle at 45% 40%,#e6dcd4,#a9988e)}

/* footer */
.site-footer{top:4780px;height:432px;background:var(--white);border-top:1px solid var(--blue-pale)}
.foot-brand{position:absolute;left:100px;top:60px}
.foot-brand .brand{position:static}
.foot-seals{display:flex;gap:14px;margin-top:30px}
.foot-seals span{width:60px;height:60px;border-radius:50%;background:var(--blue-pale)}
.foot-col{position:absolute;top:60px;font-size:12px;color:var(--muted);line-height:2}
.foot-col h5{font-family:var(--head);font-weight:800;font-size:14px;color:var(--navy);text-transform:uppercase;margin-bottom:10px}
.foot-col .btn{padding:8px 18px;font-size:11px;margin-top:8px;line-height:1.4}
.socials{display:flex;gap:8px}
.socials span{width:26px;height:26px;border-radius:50%;background:var(--navy)}
.legal{position:absolute;left:0;right:0;bottom:0;height:50px;border-top:1px solid var(--blue-pale);display:flex;align-items:center;padding:0 100px;font-size:11px;color:var(--muted)}
.legal .r{margin-left:auto}
</style>
</head>
<body>

<header class="site-header">
  <div class="topline">
    <div class="dots"><span></span><span></span><span></span><span></span></div>
    <div class="right"><span>JOIN OUR EMAIL</span><span>(212) 555-0148</span></div>
  </div>
  <div class="brand"><span class="mark"></span><span class="name">ALLIES OF<br>BEIT NORAH</span></div>
  <nav class="nav">
    <span class="active">About Us ▾</span><span>Our Impact ▾</span><span>Newsroom ▾</span><span>Contact Us</span><span>Get Involved ▾</span>
    <span class="btn btn-red">Donate Now</span>
  </nav>
</header>

<section class="hero">
  <div class="photo hero-photo" role="img" aria-label="Group of smiling volunteers and seniors gathered together"></div>
  <svg class="hero-swoop" width="1200" height="320" viewBox="0 0 1200 320" aria-hidden="true">
    <path d="M0 90 Q600 250 1200 90 L1200 320 L0 320 Z" fill="#16217a"/>
    <path d="M0 60 Q600 220 1200 60 L1200 100 Q600 260 0 100 Z" fill="#0054aa" opacity=".6"/>
  </svg>
  <div class="hero-box">
    <span class="hero-tag">Allies of Beit Norah</span>
    <h1 class="hero-title">Bring Help &amp; Hope<br>to the People of Israel</h1>
    <span class="btn">Donate Now ›</span>
  </div>
  <div class="stats">
    <div class="stat"><svg width="34" height="34" viewBox="0 0 40 40" fill="none" stroke="#fff" stroke-width="2"><circle cx="20" cy="13" r="7"/><path d="M6 36c2-9 26-9 28 0"/></svg><b>800,000</b><small>People Helped</small></div>
    <div class="stat"><svg width="34" height="34" viewBox="0 0 40 40" fill="none" stroke="#fff" stroke-width="2"><rect x="6" y="10" width="28" height="22" rx="3"/><path d="M20 15v12M14 21h12"/></svg><b>509,608</b><small>Medical Equipment Loans</small></div>
    <div class="stat"><svg width="34" height="34" viewBox="0 0 40 40" fill="none" stroke="#fff" stroke-width="2"><circle cx="13" cy="14" r="5"/><circle cx="27" cy="14" r="5"/><path d="M3 34c1-8 19-8 20 0M17 34c1-8 19-8 20 0"/></svg><b>7,000</b><small>Volunteers</small></div>
    <div class="stat"><svg width="34" height="34" viewBox="0 0 40 40" fill="none" stroke="#fff" stroke-width="2"><path d="M10 6l6 1 3 8-4 3c2 4 5 7 9 9l3-4 8 3 1 6c-14 2-28-12-26-26z"/></svg><b>297,564</b><small>Calls to Emergency Hotline</small></div>
    <div class="stat"><svg width="34" height="34" viewBox="0 0 40 40" fill="none" stroke="#fff" stroke-width="2"><path d="M20 36s-11-11-11-20a11 11 0 0122 0c0 9-11 20-11 20z"/><circle cx="20" cy="16" r="4"/></svg><b>122</b><small>Branches</small></div>
  </div>
</section>

<section class="care">
  <div class="care-ring"></div>
  <div class="photo care-photo" role="img" aria-label="Volunteer couple standing together in a clinic"></div>
  <div class="care-text">
    <div class="eyebrow">Who We Are</div>
    <h2 class="title">How We Care<br><span class="accent">for Israel's Builders</span></h2>
    <p class="copy">The defining mission of Beit Norah is to enable chronically ill, disabled, infirm, and terminally ill people, ranging in age from infancy to old age, to live at home either on their own or in the care of their families or caregivers, with dignity and as independently as possible. With the dedicated help of 7,000+ volunteers supported by a small staff and operating through over 120 branches located</p>
    <span class="btn btn-outline">Learn More ›</span>
  </div>
</section>

<section class="donate">
  <div class="photo donate-photo" role="img" aria-label="Caregiver sharing a warm moment with an elderly woman"></div>
  <div class="donate-form">
    <div class="eyebrow">Donate Now</div>
    <h2 class="title">How You Can Help</h2>
    <p>Please help the people of Israel today</p>
    <div class="amounts">
      <span class="amt">₪ 20,000</span><span class="amt">₪ 10,000</span><span class="amt">₪ 5,000</span>
      <span class="amt">₪ 2,000</span><span class="amt">₪ 1,200</span><span class="amt on">₪ 900</span>
      <span class="amt wide">₪ 500</span>
    </div>
    <div class="monthly"><i></i>Check to donate on monthly basis</div>
    <span class="btn btn-red">Donate Now ›</span>
  </div>
</section>

<section class="involved">
  <div class="involved-text">
    <div class="eyebrow">Who We Are</div>
    <h2 class="title">Get Involved <span class="accent">With Us</span></h2>
    <p class="copy">The defining mission of Beit Norah is to enable chronically ill, disabled, infirm, and terminally ill people, ranging in age from infancy to old age, to live at home either on their own or in the care of their families or caregivers, with dignity and as independently as possible. With the dedicated help of 7,000+ volunteers supported by a small staff and operating through over 120 branches located</p>
    <span class="btn btn-outline">Learn More ›</span>
  </div>
  <div class="photo involved-photo" role="img" aria-label="Seniors taking part in a group exercise class"></div>
</section>

<section class="news">
  <div class="news-head">
    <div class="eyebrow">News &amp; Blogs</div>
    <h2 class="title">The Latest of <span class="accent">Beit Norah</span></h2>
  </div>
  <div class="cards">
    <article class="card"><div class="thumb" role="img" aria-label="Volunteers at a community event"></div><div class="body"><span class="date">22 DEC 2022</span><h3>Inside Beit Norah – Fall 2022 Newsletter is Here</h3><p>We are proud to bring you another edition of our newsletter, with stories from the field and updates from every branch.</p><span class="more">Learn More</span></div></article>
    <article class="card feature"><div class="thumb" role="img" aria-label="Volunteer helping an elderly man"></div><div class="body"><span class="date">22 DEC 2022</span><h3>Inside Beit Norah – Fall 2022 Newsletter is Here</h3><p>We are proud to bring you another edition of our newsletter, with stories from the field and updates from every branch.</p><span class="more">Learn More</span></div></article>
    <article class="card"><div class="thumb" role="img" aria-label="Family visiting a grandparent at home"></div><div class="body"><span class="date">22 DEC 2022</span><h3>Inside Beit Norah – Fall 2022 Newsletter is Here</h3><p>We are proud to bring you another edition of our newsletter, with stories from the field and updates from every branch.</p><span class="more">Learn More</span></div></article>
  </div>
</section>

<section class="impact">
  <div class="impact-frame"></div>
  <div class="photo impact-photo" role="img" aria-label="Elderly man playing guitar and singing"></div>
  <div class="impact-text">
    <div class="eyebrow">Our Impact</div>
    <h2 class="title">The Impact of <span class="accent">Your Support</span></h2>
    <div class="point"><span class="dot"><svg width="22" height="22" viewBox="0 0 22 22"><path d="M11 2l2.7 6 6.3.6-4.8 4.2 1.5 6.2L11 15.8 5.3 19l1.5-6.2L2 8.6 8.3 8z" fill="#fff"/></svg></span><div><h4>4-Stars for 9 Years</h4><p>Allies of Beit Norah has earned a 4-star rating from Charity Compass for the ninth consecutive year. We are proud to have our high standards seen.</p></div></div>
    <div class="point"><span class="dot"><svg width="22" height="22" viewBox="0 0 22 22" fill="none" stroke="#fff" stroke-width="2.2"><path d="M4 18V10M10 18V5M16 18v-6"/></svg></span><div><h4>Beit Norah's Vital Statistics</h4><p>Today, nearly 60 years after it was founded, Beit Norah has over 120 branches throughout Israel staffed by more than 7,000 volunteers.</p></div></div>
    <span class="btn btn-outline">Learn More ›</span>
  </div>
</section>

<section class="profile">
  <div class="profile-head">
    <div class="eyebrow">Our Impact</div>
    <h2 class="title">Our <span class="accent">Profile</span></h2>
  </div>
  <div class="badges">
    <div class="badge-card"><div class="seal"></div><h4>Clearview Giving Revolutionizes</h4><p>Clearview Giving revolutionizes philanthropy by providing information that advances transparency so donors can make better decisions.</p></div>
    <div class="badge-card"><div class="plate"></div><h4>Charity Compass Rating</h4><p>Allies of Beit Norah earned a 2020 four-star rating, its ninth consecutive 4-star rating from Charity Compass.</p></div>
  </div>
</section>

<section class="contact">
  <div class="contact-text">
    <div class="eyebrow">Connect With Us</div>
    <h2 class="title">Get In <span class="accent">Touch With Us</span></h2>
    <div class="line"><span class="ic"><svg width="18" height="18" viewBox="0 0 40 40"><path d="M10 6l6 1 3 8-4 3c2 4 5 7 9 9l3-4 8 3 1 6c-14 2-28-12-26-26z" fill="#fff"/></svg></span><div><small>Phone number</small><span>(212) 555-0148</span></div></div>
    <div class="line"><span class="ic"><svg width="18" height="18" viewBox="0 0 20 20" fill="none" stroke="#fff" stroke-width="2"><rect x="2" y="4" width="16" height="12"/><path d="M2 4l8 7 8-7"/></svg></span><div><small>Email us</small><span>info@alliesofbeitnorah.example</span></div></div>
    <div class="line"><span class="ic"><svg width="18" height="18" viewBox="0 0 40 40"><path d="M20 38s-12-12-12-22a12 12 0 0124 0c0 10-12 22-12 22z" fill="#fff"/></svg></span><div><small>Location</small><span>120 Harbor Lane, Suite 400,<br>New York, NY 10001 USA</span></div></div>
    <p class="subscribe-label">Please subscribe below to receive our latest updates.</p>
    <div class="subscribe"><span>Email address...</span><b>Subscribe Now</b></div>
  </div>
  <div class="contact-ring"></div>
  <div class="photo contact-photo" role="img" aria-label="Smiling elderly woman portrait"></div>
</section>

<footer class="site-footer">
  <div class="foot-brand">
    <div class="brand"><span class="mark"></span><span class="name">ALLIES OF<br>BEIT NORAH</span></div>
    <div class="foot-seals"><span></span><span></span></div>
  </div>
  <div class="foot-col" style="left:430px"><h5>Navigation</h5>About Us<br>Our Impact<br>Newsroom<br>Get Involved<br>Donate Now<br>Contact Us</div>
  <div class="foot-col" style="left:620px;width:220px"><h5>Support Now</h5>Your gift will help provide a wide array of compassionate health and home care services for people of all ages in Israel.<br><span class="btn btn-red">Donate Now</span></div>
  <div class="foot-col" style="left:880px;width:240px"><h5>Contact Us</h5>Allies of Beit Norah, Inc.<br>120 Harbor Lane, Suite 400<br>info@alliesofbeitnorah.example<br>(212) 555-0148<br>Get directions</div>
  <div class="foot-col" style="left:880px;top:300px"><div class="socials"><span></span><span></span><span></span><span></span></div></div>
  <div class="legal"><span>Copyright © 2023 Allies of Beit Norah. All rights reserved.</span><span class="r">Privacy Policy &nbsp;|&nbsp; Terms of Use</span></div>
</footer>

</body>
</html>
```